Bref créative
New Corporate Website - Blue Falcons
Blue Falcons - Marketing & Lead Generation
Marketing
Does not yet exist
Blue Falcons is a new Marketing and Sales Lead generation agency specializing in helping companies analyze, pursue and close sales opportunities generated via the Internet. We provide access to our exclusive Blue Falcon Striker platform for capturing and pursing sales opportunities generated via the online platform.
I'd like to showcase a lot of red on this website. This is a new website for a new company we are starting.
The website is to feature both our online web software as well as our consulting services.
High Tech
Red (#aa0000)
Grey (#cccccc)
Verdana
Century Gothic
top
http://www.vortelix.com
http://www.brinaxo.com/en
http://www.quombrel.com
The page should include links for
Navigation
- About Blue Falcons
- Services & Solutions
- Results
- News & Announcements
- Contact Us
Also, an area for current customer's to login
please incorporate the logo of the man riding the horse backwards.

```html
<!DOCTYPE html>
<html lang="en">
<head>
<meta charset="utf-8">
<title>Blue Falcons - Marketing &amp; Lead Generation</title>
<link href="https://fonts.googleapis.com/css2?family=Questrial&family=Open+Sans:ital,wght@0,400;0,700;1,400&display=swap" rel="stylesheet">
<style>
  :root {
    --red: #aa0000;
    --red-deep: #8c0000;
    --red-bright: #c41010;
    --grey: #cccccc;
    --grey-light: #e9e9e9;
    --grey-text: #8a8a8a;
    --white: #ffffff;
    --ink: #222222;
  }
  * { box-sizing: border-box; margin: 0; padding: 0; }
  html, body { width: 1200px; height: 821px; overflow: hidden; }
  body {
    position: relative;
    font-family: "Open Sans", sans-serif;
    background: var(--white);
    color: var(--white);
  }
  .backdrop {
    position: absolute; left: 0; top: 72px; width: 1200px; height: 680px;
    background: linear-gradient(180deg, #d6d6d6 0%, #bdbdbd 45%, #e4e4e4 80%, #ffffff 100%);
  }
  .site-header {
    position: absolute; left: 0; top: 0; width: 1200px; height: 72px;
    background: linear-gradient(180deg, var(--red-bright) 0%, var(--red) 100%);
  }
  .brand {
    position: absolute; left: 130px; top: 10px;
    font-family: "Questrial", sans-serif; font-size: 40px; color: var(--white);
  }
  .main-nav a {
    position: absolute; top: 24px;
    font-family: "Questrial", sans-serif; font-size: 17px; color: var(--white); text-decoration: none;
  }
  .content-panel {
    position: absolute; left: 132px; top: 91px; width: 943px; height: 619px;
    background: linear-gradient(135deg, var(--red-deep) 0%, var(--red) 40%, var(--red-bright) 100%);
  }
  .feature-tile {
    position: absolute; top: 108px; width: 240px; height: 252px; overflow: hidden;
    box-shadow: 0 4px 10px rgba(0,0,0,.35);
  }
  .feature-tile .visual { position: absolute; inset: 0; }
  .tile-marketing .visual { background: radial-gradient(circle at 55% 35%, #ffffff 0 18%, #b51010 19%, #6a0000 100%); }
  .tile-leads .visual { background: radial-gradient(circle at 50% 55%, #d01818 0 14%, #e8e8e8 15%, #a9a9a9 100%); }
  .feature-caption {
    position: absolute; left: 0; bottom: 0; width: 100%; height: 66px;
    background: rgba(255,255,255,.72); padding: 6px 8px;
    font-family: "Questrial", sans-serif; font-size: 22px; line-height: 26px; color: var(--red);
  }
  .intro { position: absolute; left: 732px; top: 134px; width: 320px; }
  .intro h2 { font-size: 24px; font-weight: 700; margin-bottom: 10px; }
  .intro p { font-size: 11px; font-style: italic; line-height: 13.5px; }
  .login { position: absolute; left: 156px; top: 400px; width: 240px; }
  .login h2 { font-size: 25px; font-weight: 700; margin-bottom: 18px; }
  .login-row { display: flex; align-items: center; height: 32px; }
  .login-row label { width: 84px; font-size: 12px; font-weight: 700; }
  .login-row input { width: 126px; height: 19px; border: 1px solid var(--grey); background: var(--white); }
  .login-actions { margin-left: 84px; margin-top: 8px; display: flex; gap: 6px; }
  .login-actions button {
    font-family: "Open Sans", sans-serif; font-size: 11px; padding: 1px 8px;
    background: var(--red-deep); color: var(--white); border: 1px solid var(--white);
  }
  .article { position: absolute; left: 432px; top: 400px; width: 628px; }
  .article h1 { font-size: 23px; font-weight: 700; margin-bottom: 14px; }
  .article p { font-size: 11.2px; line-height: 13.6px; margin-bottom: 18px; }
  .site-footer {
    position: absolute; left: 130px; top: 752px; width: 945px;
    font-size: 11px; color: var(--grey-text);
  }
  .footer-nav { position: absolute; right: 0; top: 0; display: flex; gap: 14px; }
  .footer-nav a { color: var(--grey-text); text-decoration: none; }
</style>
</head>
<body>
  <div class="backdrop" role="img" aria-label="Grey background of large embossed 3D letters"></div>

  <header class="site-header">
    <div class="brand">Blue Falcons</div>
    <nav class="main-nav">
      <a href="#" style="left:384px">About Blue Falcons</a>
      <a href="#" style="left:560px">Services &amp; Solutions</a>
      <a href="#" style="left:718px">Results News &amp; Announcements</a>
      <a href="#" style="left:980px">Contact Us</a>
    </nav>
  </header>

  <main class="content-panel"></main>

  <div class="feature-tile tile-marketing" style="left:156px">
    <div class="visual" role="img" aria-label="Gloved hand holding up a blank white card on a red background"></div>
    <div class="feature-caption">Blue Falcons<br>Marketing</div>
  </div>
  <div class="feature-tile tile-leads" style="left:432px">
    <div class="visual" role="img" aria-label="One red sphere among many white spheres"></div>
    <div class="feature-caption">Blue Falcons<br>Lead Generation</div>
  </div>

  <section class="intro">
    <h2>Lorem ipsum</h2>
    <p>"Lorem ipsum dolor sit amet, consectetur adipisicing elit, sed do eiusmod tempor incididunt ut labore et dolore magna aliqua. Ut enim ad minim veniam, quis nostrud exercitation ullamco laboris nisi ut aliquip ex ea commodo consequat. Duis aute irure dolor in reprehenderit in voluptate velit esse cillum dolore eu fugiat nulla pariatur. Excepteur sint occaecat cupidatat non proident, sunt in culpa qui officia deserunt mollit anim id est laborum."</p>
  </section>

  <section class="login">
    <h2>User login</h2>
    <div class="login-row"><label>User name:</label><input type="text"></div>
    <div class="login-row"><label>Password:</label><input type="password"></div>
    <div class="login-actions"><button>Login</button><button>Register</button></div>
  </section>

  <article class="article">
    <h1>Blue Falcons - Marketing &amp; Lead Generation</h1>
    <p>Contrary to popular belief, Lorem Ipsum is not simply random text. It has roots in a piece of classical Latin literature from 45 BC, making it over 2000 years old. Daniel Orrin, a Latin professor at Westbrook College in Virginia, looked up one of the more obscure Latin words, consectetur, from a Lorem Ipsum passage, and going through the cites of the word in classical literature, discovered the undoubtable source. Lorem Ipsum comes from sections 1.10.32 and 1.10.33 of "de Finibus Bonorum et Malorum" (The Extremes of Good and Evil) by Varonius, written in 45 BC. This book is a treatise on the theory of ethics, very popular during the Renaissance. The first line of Lorem Ipsum, "Lorem ipsum dolor sit amet..", comes from a line in section 1.10.32.</p>
    <p>The standard chunk of Lorem Ipsum used since the 1500s is reproduced below for those interested. Sections 1.10.32 and 1.10.33 from "de Finibus Bonorum et Malorum" by Varonius are also reproduced in their exact original form, accompanied by English versions from the 1914 translation by T. Ellory.</p>
  </article>

  <footer class="site-footer">
    <span>Copyright © 2011 Blue Falcons. All Rights Reserved.</span>
    <nav class="footer-nav">
      <a href="#">About Blue Falcons</a>
      <a href="#">Services &amp; Solutions</a>
      <a href="#">Results</a>
      <a href="#">News &amp; Announcements</a>
      <a href="#">Contact Us</a>
    </nav>
  </footer>
</body>
</html>
```